Crestline Gas and Plumbing Business Card Design

I am after a business card design for my plumbing business called 'Crestline Gas & Plumbing'. I do all types of plumbing and gas work and specialise in general maintenance plumbing. Would like to see designs using current logo

Industry/Entity Type

Plumbing

Contact Information for Business Card

Name - Dale Whitcombe
Phone number - 0455163027
Email - admin@crestlinegasandplumbing.example.com.au
ABN - 68204915336

```html
<!DOCTYPE html>
<html lang="en">
<head>
<meta charset="utf-8">
<title>Crestline Gas &amp; Plumbing – Business Card</title>
<link rel="stylesheet" href="https://fonts.googleapis.com/css2?family=Arimo:wght@400;700&display=swap">
<style>
  :root {
    --bg: #e9e9e9;
    --navy: #173f7e;
    --white: #ffffff;
    --card-white: #f8f8f8;
    --orange: #ef9712;
    --brand-blue: #1f5aa8;
    --ink: #111111;
    --rule: #e6a24a;
  }
  * { box-sizing: border-box; margin: 0; padding: 0; }
  html, body {
    width: 1200px; height: 800px; overflow: hidden;
    background: var(--bg);
    font-family: "Arimo", Arial, sans-serif;
  }
  .canvas { position: relative; width: 1200px; height: 800px; }
  .card {
    position: absolute; top: 278px;
    width: 420px; height: 240px;
  }
  .card--front { left: 141px; background: var(--navy); }
  .card--back { left: 637px; background: var(--card-white); }

  .front-brand {
    position: absolute; left: 0; right: 0; top: 0; bottom: 0;
    display: flex; align-items: center; justify-content: center; gap: 14px;
    color: var(--white);
  }
  .front-brand__dot {
    width: 38px; height: 38px; border-radius: 50%; background: var(--white);
  }
  .front-brand__name {
    font-weight: 700; font-size: 25px; line-height: 1.1; text-transform: uppercase;
  }

  .holder-name {
    position: absolute; left: 43px; top: 55px;
    font-weight: 700; font-size: 19px; color: var(--orange);
  }
  .back-brand {
    position: absolute; right: 45px; top: 50px;
    display: flex; align-items: center; gap: 7px;
    color: var(--brand-blue);
  }
  .back-brand__dot {
    width: 22px; height: 22px; border-radius: 50%; background: var(--brand-blue);
  }
  .back-brand__name {
    font-weight: 700; font-size: 12px; line-height: 1.15; text-transform: uppercase;
  }
  .divider {
    position: absolute; left: 43px; top: 113px; width: 332px; height: 1px;
    background: var(--rule);
  }
  .contact {
    position: absolute; left: 43px; list-style: none;
    display: flex; align-items: center; gap: 6px;
    color: var(--ink);
  }
  .contact--phone { top: 133px; font-size: 16px; }
  .contact--email { top: 156px; font-size: 13.2px; }
  .contact__icon { width: 14px; height: 14px; flex: none; }
  .abn {
    position: absolute; right: 45px; top: 181px;
    font-size: 13px; color: var(--ink);
  }
</style>
</head>
<body>
<main class="canvas">
  <section class="card card--front" aria-label="Card front">
    <div class="front-brand">
      <span class="front-brand__dot"></span>
      <span class="front-brand__name">Crestline<br>Gas &amp; Plumbing</span>
    </div>
  </section>

  <section class="card card--back" aria-label="Card back">
    <p class="holder-name">Dale Whitcombe</p>
    <div class="back-brand">
      <span class="back-brand__dot"></span>
      <span class="back-brand__name">Crestline<br>Gas &amp; Plumbing</span>
    </div>
    <div class="divider"></div>

    <p class="contact contact--phone">
      <svg class="contact__icon" viewBox="0 0 14 14" aria-hidden="true">
        <rect x="0" y="2" width="14" height="10" rx="1" fill="#ef9712"/>
        <path d="M0.5 2.8 L7 7.5 L13.5 2.8" fill="none" stroke="#fff" stroke-width="1.2"/>
      </svg>
      0455163027
    </p>
    <p class="contact contact--email">
      <svg class="contact__icon" viewBox="0 0 14 14" aria-hidden="true">
        <circle cx="7" cy="7" r="7" fill="#ef9712"/>
        <path d="M4.6 3.6 l1.3 -0.3 l0.8 2 l-0.9 0.7 a5 5 0 0 0 2.2 2.2 l0.7 -0.9 l2 0.8 l-0.3 1.3 a1 1 0 0 1 -1 0.7 a6.4 6.4 0 0 1 -5.5 -5.5 a1 1 0 0 1 0.7 -1 z" fill="#fff"/>
      </svg>
      admin@crestlinegasandplumbing.example.com.au
    </p>
    <p class="abn">ABN - 68204915336</p>
  </section>
</main>
</body>
</html>
```